Business card required for IT Consultancy Business - Tealbrook Consulting.
Company provides the whole nine yards of services across IT Architecture, design and execution.
Basically we provide consulting services to help businesses make sure their technology is enabling their business strategy.
Design for front and back required.
We would like the front of the card to inlcude:
Name
Title
Mobile number
email address
www.tbkc.com.au
Company logos attached.
Thank you
Industry/Entity Type
Business
Contact Information for Business Card
Name
Title
Mobile number
email address
www.tbkc.com.au
Look and feel
Each slider illustrates characteristics of the customer's brand and the style your logo design should communicate.

```html
<!DOCTYPE html>
<html lang="en">
<head>
<meta charset="utf-8">
<title>Tealbrook Consulting — Business Cards</title>
<link rel="stylesheet" href="https://fonts.googleapis.com/css2?family=Montserrat:wght@700&family=Jost:wght@400;500&family=Lato:wght@400&display=swap">
<style>
  :root {
    --brand-blue: #1f74c2;
    --brand-orange: #ee5a2a;
    --card-white: #ffffff;
    --ink: #2a2a2a;
    --backdrop: #3b3c3e;
  }
  * { box-sizing: border-box; margin: 0; padding: 0; }
  html, body { width: 1200px; height: 1000px; overflow: hidden; }
  body {
    background: var(--backdrop);
    display: flex;
    flex-direction: column;
    align-items: center;
    justify-content: center;
    gap: 36px;
  }
  .card {
    position: relative;
    width: 760px;
    height: 434px;
    background: var(--card-white);
    overflow: hidden;
  }
  .wordmark {
    font-family: "Montserrat", sans-serif;
    font-weight: 700;
    color: var(--brand-blue);
    display: flex;
    align-items: center;
    gap: 12px;
    white-space: nowrap;
  }
  .wordmark__dot {
    width: 20px; height: 20px;
    border-radius: 50%;
    background: var(--brand-orange);
    flex: none;
  }
  /* Back */
  .card--back .wordmark {
    position: absolute;
    left: 50%; top: 150px;
    transform: translateX(-50%);
    font-size: 36px;
  }
  .card--back .web {
    position: absolute;
    left: 0; right: 0; bottom: 52px;
    text-align: center;
    font-family: "Jost", sans-serif;
    font-size: 17px;
    letter-spacing: 3px;
    color: var(--brand-blue);
  }
  /* Front */
  .card__wave { position: absolute; inset: 0; }
  .card--front .wordmark {
    position: absolute;
    left: 58px; top: 98px;
    font-size: 28px;
  }
  .address {
    position: absolute;
    left: 38px; top: 272px;
    font-family: "Lato", sans-serif;
    font-size: 20px;
    line-height: 1.35;
    color: var(--ink);
  }
  .contact {
    position: absolute;
    right: 30px; top: 128px;
    text-align: right;
    color: var(--card-white);
    font-family: "Jost", sans-serif;
  }
  .contact__name { font-size: 26px; font-weight: 500; letter-spacing: 0.5px; line-height: 1; margin-right: 8px; }
  .contact__title { font-size: 17px; margin-top: 4px; margin-right: 34px; }
  .contact__list { list-style: none; margin-top: 30px; font-size: 18px; }
  .contact__list li { display: flex; justify-content: flex-end; align-items: center; gap: 10px; line-height: 1.5; }
  .icon { width: 15px; height: 15px; flex: none; }
</style>
</head>
<body>
  <section class="card card--back">
    <div class="wordmark"><span class="wordmark__dot"></span>Tealbrook Consulting</div>
    <p class="web">www.tbkc.com.au</p>
  </section>

  <section class="card card--front">
    <svg class="card__wave" viewBox="0 0 760 434" aria-hidden="true">
      <path transform="translate(-18,-14)" fill="var(--brand-orange)" d="M760,0 L680,0 C560,10 520,130 480,240 C440,370 300,395 0,400 L0,470 L800,470 L800,0 Z"/>
      <path transform="translate(-9,-7)" fill="var(--card-white)" d="M760,0 L680,0 C560,10 520,130 480,240 C440,370 300,395 0,400 L0,470 L800,470 L800,0 Z"/>
      <path fill="var(--brand-blue)" d="M760,0 L680,0 C560,10 520,130 480,240 C440,370 300,395 0,400 L0,470 L800,470 L800,0 Z"/>
    </svg>

    <div class="wordmark"><span class="wordmark__dot"></span>Tealbrook Consulting</div>

    <p class="address">Your Street Address Here,<br>Australia, 1234</p>

    <div class="contact">
      <p class="contact__name">DANIEL REEVE</p>
      <p class="contact__title">Founder/CEO</p>
      <ul class="contact__list">
        <li>(000) 284-7316
          <svg class="icon" viewBox="0 0 16 16"><path fill="#fff" d="M3 1l3 3-2 2c1 2 3 4 5 5l2-2 3 3-2 3C6 15 1 10 1 3z"/></svg>
        </li>
        <li>daniel@tbkc.com.au
          <svg class="icon" viewBox="0 0 16 16"><rect x="1" y="3" width="14" height="10" fill="#fff"/><path d="M1 3l7 6 7-6" fill="none" stroke="#1f74c2" stroke-width="1.5"/></svg>
        </li>
        <li>www.tbkc.com.au
          <svg class="icon" viewBox="0 0 16 16"><circle cx="8" cy="8" r="6.5" fill="none" stroke="#fff" stroke-width="1.5"/><path d="M1.5 8h13M8 1.5c-3 3.5-3 9.5 0 13M8 1.5c3 3.5 3 9.5 0 13" fill="none" stroke="#fff" stroke-width="1.2"/></svg>
        </li>
      </ul>
    </div>
  </section>
</body>
</html>
```